Tempest Sealer - Postcard

tempestsealer.com

Tel ‪(941) 508-3174‬

Daniel Prewitt
daniel@tempestsealer.com

Design a postcard for a marketing campaign.

The problem is that all roofing vents leak. We have a product that goes into the vent that stops the roof from leaking.

In the last hurricane here in Florida, many houses were damaged because of water coming into the attic from the vents. The tempest sealer is a device that stops water from coming into the vents. This prevents water damage in the house. This stops mold from forming in the attic.

The tempest sealer offers this solution. It stops the rainwater from entering the roof through the roof vents. It stops water damages from occurring in the house which can cost 10s of thousands of dollars.

The target customer is a affluent, older couple 50-60 years old.

Target Market(s)

middle class to upper class adults / ages 50-60 years old (older but not VERY old)

Industry/Entity Type

roofing and construction

Font styles to use
Sans Serif

Colors
0054AA
0677BA
7BADD7
CADEEF
E8F1F8
0094D4
00A9DD
6FCCEA
C7EBF8
E9F6FB
FFF300
FFF600
FEFA6F
FFFEC7
FFFEE8
F0912C
F2A743
F7CA91
FBE8D2
FDF5EE

Requirements
Must have
• images of rain, wind, storm roofing, leaks, wet house, rain through interior ceilings, anxiety, storm damage
Nice to have
• feelings: professional / strong / reliable / safety / shelter / security / future stability

```html
<!DOCTYPE html>
<html lang="en">
<head>
<meta charset="utf-8">
<title>Tempest Sealer – Postcard</title>
<link rel="stylesheet" href="https://fonts.googleapis.com/css2?family=Source+Sans+3:wght@300;400;600;700&display=swap">
<style>
  :root{
    --blue-deep:#0054AA;
    --blue-mid:#0677BA;
    --blue-pale:#CADEEF;
    --orange:#F0912C;
    --cream:#F6F2EC;
    --tile-dark:#6E3A2C;
    --tile-light:#A8644C;
    --page:#E9E6E2;
  }
  *{margin:0;padding:0;box-sizing:border-box}
  html,body{width:831px;height:1200px;overflow:hidden;background:var(--page)}
  .postcard{position:relative;width:831px;height:1200px;overflow:hidden;font-family:"Source Sans 3",sans-serif}
  .artwork{position:absolute;inset:0}
  .call-line{position:absolute;left:66px;top:368px;font-size:34px;font-weight:400;color:var(--blue-deep);letter-spacing:.2px}
  .intro,.solution{position:absolute;width:300px;font-size:20px;line-height:29px;font-weight:300;color:var(--orange);text-align:justify}
  .intro{left:72px;top:418px}
  .problem{position:absolute;left:58px;top:682px;width:480px;font-size:21.5px;line-height:30px;font-weight:700;color:var(--orange)}
  .solution{left:56px;top:866px;width:290px}
  .brand{position:absolute;left:470px;top:852px;width:170px;text-align:center}
  .brand-dot{display:block;width:44px;height:44px;margin:0 auto 8px;border-radius:50%;background:var(--blue-mid)}
  .brand-name{font-size:26px;font-weight:600;color:var(--blue-deep);line-height:1}
  .contact-band{position:absolute;left:42px;top:1126px;font-size:21px;line-height:28px;font-weight:600;color:var(--blue-deep)}
</style>
</head>
<body>
<main class="postcard">
  <svg class="artwork" width="831" height="1200" viewBox="0 0 831 1200">
    <defs>
      <linearGradient id="roofTiles" x1="0" y1="0" x2="1" y2="1">
        <stop offset="0" stop-color="#7A4233"/>
        <stop offset=".5" stop-color="#9B5A45"/>
        <stop offset="1" stop-color="#6E3A2C"/>
      </linearGradient>
      <linearGradient id="ventRoof" x1="0" y1="0" x2="1" y2="1">
        <stop offset="0" stop-color="#D9CDBD"/>
        <stop offset=".6" stop-color="#C3B4A0"/>
        <stop offset="1" stop-color="#E9E6E0"/>
      </linearGradient>
      <linearGradient id="ceilingRepair" x1="0" y1="0" x2="1" y2="1">
        <stop offset="0" stop-color="#E2C9A6"/>
        <stop offset=".6" stop-color="#D49B6A"/>
        <stop offset="1" stop-color="#E0762C"/>
      </linearGradient>
      <linearGradient id="damagedHouse" x1="0" y1="0" x2="1" y2="1">
        <stop offset="0" stop-color="#5E8A4A"/>
        <stop offset=".5" stop-color="#B9C0C4"/>
        <stop offset="1" stop-color="#4A5A4A"/>
      </linearGradient>
      <linearGradient id="couplePortrait" x1="0" y1="0" x2="1" y2="1">
        <stop offset="0" stop-color="#8FA968"/>
        <stop offset=".5" stop-color="#E2C2A8"/>
        <stop offset="1" stop-color="#4E5870"/>
      </linearGradient>
    </defs>

    <rect class="roof-backdrop" width="831" height="760" fill="url(#roofTiles)" role="img" aria-label="Wet clay roof tiles in the rain"/>

    <polygon class="text-panel" points="0,336 253,142 831,720 831,1200 0,1200" fill="var(--cream)"/>

    <polygon class="photo-ceiling" points="407,0 540,144 407,288 274,144" fill="url(#ceilingRepair)" role="img" aria-label="Worker repairing a water-stained ceiling"/>
    <polygon class="photo-house" points="690,20 831,40 831,330 690,340 540,180" fill="url(#damagedHouse)" role="img" aria-label="Storm-damaged house roof among trees"/>
    <polygon class="photo-vent" points="400,600 731,290 831,384 831,820 731,918" fill="url(#ventRoof)" role="img" aria-label="Sealed roof vent on a tiled roof"/>
    <polygon class="photo-couple" points="510,1150 740,920 831,1011 831,1200 560,1200" fill="url(#couplePortrait)" role="img" aria-label="Smiling older couple outdoors"/>

    <polygon class="contact-band-shape" points="0,1116 530,1116 560,1200 0,1200" fill="var(--blue-pale)"/>
  </svg>

  <h1 class="call-line">Call Us (941) 508-3174</h1>

  <p class="intro">In the last hurricane here in Florida, many houses were damaged because of water coming into the attic from the vents. The tempest sealer is a device that stops water from coming into the vents. This prevents water damage in the house. This stops mold from forming in the attic.</p>

  <p class="problem">The problem is that all roofing vents leak.<br>We have a product that goes into the vent<br>that stops the roof from leaking.</p>

  <p class="solution">The tempest sealer offers this solution. It stops the rainwater from entering the roof through the roof vents. It stops water damages from occurring in the house which can cost 10s of thousands of dollars.</p>

  <div class="brand">
    <span class="brand-dot"></span>
    <span class="brand-name">Tempest Sealer</span>
  </div>

  <p class="contact-band">More Info: www.tempestsealer.com<br>Email: daniel@tempestsealer.com</p>
</main>
</body>
</html>
```